Rack Card Design Project

We are a locally family owned public golf course. We would like to have a rack card designed that can be used for multiple applications. The colors in our logo are grey, blue, and white. Please use those in the card design. The company logo, contact information, address, and summer pricing should be included. I've included some pictures that may or may not be used. I'm also open to suggestions....use one photo, multiple photos, a stock photo or image representing golf etc.

```html
<!DOCTYPE html>
<html lang="en">
<head>
<meta charset="utf-8">
<title>Heron Bay Golf Club Rack Card</title>
<link href="https://fonts.googleapis.com/css2?family=Carlito:wght@400;700&family=Crimson+Text:wght@700&display=swap" rel="stylesheet">
<style>
:root{
  --stage:#444546;
  --navy:#1a3c6e;
  --navy-deep:#12305c;
  --grey:#9a9a9b;
  --grey-light:#a6a6a7;
  --white:#ffffff;
  --ink:#1c2e52;
}
*{margin:0;padding:0;box-sizing:border-box}
html,body{width:1200px;height:1200px;overflow:hidden;background:var(--stage)}
body{position:relative;font-family:"Carlito",Calibri,sans-serif}
.card{position:absolute;overflow:hidden;box-shadow:6px 6px 10px rgba(0,0,0,.45)}
.card svg.art{position:absolute;left:0;top:0}
.abs{position:absolute}

/* front */
.front{left:82px;top:82px;width:474px;height:1031px;background:var(--white)}
.club-mark{left:0;width:100%;top:82px;display:flex;align-items:center;justify-content:center;gap:10px;
  font-family:"Crimson Text",serif;font-weight:700;font-size:24px;color:var(--navy)}
.club-mark .dot{width:24px;height:24px;border-radius:50%;background:var(--grey)}
.welcome{left:0;width:100%;top:180px;text-align:center;font-family:"Crimson Text",serif;font-weight:700;
  font-size:43px;line-height:46px;color:var(--navy);letter-spacing:-.5px}
.about{left:17px;width:432px;top:726px;font-size:14px;line-height:18.5px;color:var(--white);text-align:justify}
.visit{left:0;width:100%;top:908px;display:flex;align-items:center;color:var(--white);font-weight:700;font-size:24px}
.visit .rule{height:2px;background:var(--white);flex:1}
.visit span{padding:0 14px}
.front-foot{left:0;width:100%;top:951px;text-align:center;font-size:14px;line-height:19px;color:#111}
.front-foot .contacts{display:flex;justify-content:center;gap:58px;margin-top:5px}
.ico{display:inline-block;vertical-align:-3px;margin-right:8px}

/* back */
.back{left:646px;top:77px;width:476px;height:1036px;background:var(--navy)}
.rates-title{left:0;width:100%;top:20px;text-align:center;font-weight:700;font-size:33px;color:var(--white)}
.band{left:0;width:100%;background:var(--grey-light);color:var(--white);text-align:center}
.season{top:64px;height:39px;font-size:25px;line-height:39px}
.full-box{left:66px;top:143px;width:327px;height:178px;border:1.5px solid var(--white)}
.box-label{border:1.5px solid var(--white);background:var(--navy);color:var(--white);text-align:center}
.full-title{left:98px;top:117px;width:260px;height:53px;font-size:28px;line-height:50px}
.tee-times,.tee-prices{top:184px;font-size:25px;line-height:37px;color:var(--white)}
.tee-times{left:114px}
.tee-prices{left:228px}
.divider{left:206px;top:181px;width:2px;height:113px;background:var(--white)}
.nine{left:68px;top:345px;width:321px;height:53px;font-size:28px;line-height:50px}
.walking{left:129px;top:420px;width:189px;height:47px;font-size:28px;line-height:44px}
.kids{top:498px;height:80px;font-size:27px;line-height:37px;padding-top:4px}
.lunch{left:0;width:100%;top:594px;text-align:center;font-size:26px;color:var(--white)}
.lunch-hours{left:129px;top:630px;width:204px;height:34px;border-radius:17px;background:var(--grey-light);
  color:var(--white);text-align:center;font-size:28px;line-height:34px}
.back-contact{left:0;width:100%;text-align:center;font-size:14.5px;color:var(--white)}
.back-foot{left:0;width:100%;top:980px;text-align:center;font-size:14px;line-height:19px;color:var(--white)}
</style>
</head>
<body>

<section class="card front">
  <svg class="art" width="474" height="1031" viewBox="0 0 474 1031">
    <defs>
      <linearGradient id="frontBlue" x1="0" y1="0" x2="1" y2="1">
        <stop offset="0" stop-color="#12305c"/><stop offset=".5" stop-color="#1f4a80"/><stop offset="1" stop-color="#12305c"/>
      </linearGradient>
      <linearGradient id="fairway" x1="0" y1="0" x2="0" y2="1">
        <stop offset="0" stop-color="#6f8f55"/><stop offset=".3" stop-color="#6e9f4a"/><stop offset=".65" stop-color="#3d6a2b"/><stop offset="1" stop-color="#8a8468"/>
      </linearGradient>
    </defs>
    <rect x="0" y="600" width="474" height="340" fill="url(#frontBlue)"/>
    <ellipse cx="237" cy="494" rx="292" ry="206" fill="var(--grey)"/>
    <ellipse cx="237" cy="494" rx="284" ry="196" fill="url(#fairway)" role="img" aria-label="Photo of a green fairway with palms, oaks and ornamental grasses"/>
  </svg>

  <div class="abs club-mark"><span class="dot"></span>Heron Bay Golf Club</div>
  <h1 class="abs welcome">Welcome to The Shores<br>of Heron Bay Golf Club</h1>

  <p class="abs about">This par 66 course features that old Florida look with southern oak and pine trees. The designated green space has very little sand, but the water hazards and some tight fairways will provide a challenging golf experience. Designed by Harlan Pruett under the original name of Cedar Lakes Golf Club measures 4345 from the the back tees. There are 6 par 3s and 12 par 4s. Located north of the Cypress Bridge in Palmview Fl, in the Heron Bay Shores subdivision, west of rt. 1 and 1 block off the North Fork of the Laurel River. Renamed Heron Bay Golf Club in 2014.</p>

  <div class="abs visit"><i class="rule"></i><span>COME VISIT US TODAY.</span><i class="rule"></i></div>

  <div class="abs front-foot">
    <div><svg class="ico" width="14" height="18" viewBox="0 0 14 18"><path d="M7 0a7 7 0 0 0-7 7c0 5 7 11 7 11s7-6 7-11a7 7 0 0 0-7-7zm0 10a3 3 0 1 1 0-6 3 3 0 0 1 0 6z" fill="var(--navy)"/></svg>The Shores of Heron Bay Golf Club, 2450 NW Cypress Lake Dr<br>Palmview, FL 30012</div>
    <div class="contacts">
      <span><svg class="ico" width="16" height="16" viewBox="0 0 16 16"><circle cx="8" cy="8" r="7" fill="none" stroke="var(--navy)" stroke-width="1.3"/><path d="M5.5 4.5l1.5 1.6-.8 1c.5 1 1.3 1.8 2.3 2.3l1-.8 1.6 1.5-.9 1.2c-2.6-.4-4.7-2.5-5.1-5.1z" fill="var(--navy)"/></svg>555-014-0272</span>
      <span><svg class="ico" width="14" height="14" viewBox="0 0 14 14"><g fill="none" stroke="var(--navy)" stroke-width="1.1"><circle cx="7" cy="7" r="6"/><ellipse cx="7" cy="7" rx="2.6" ry="6"/><path d="M1 7h12M2 4h10M2 10h10"/></g></svg>www.heronbaygc.com</span>
    </div>
  </div>
</section>

<section class="card back">
  <svg class="art" width="476" height="1036" viewBox="0 0 476 1036">
    <defs>
      <linearGradient id="dusk" x1="0" y1="0" x2="0" y2="1">
        <stop offset="0" stop-color="#6b6c52"/><stop offset=".35" stop-color="#3f4a2c"/><stop offset=".7" stop-color="#3b5a2a"/><stop offset="1" stop-color="#2a4020"/>
      </linearGradient>
    </defs>
    <rect x="0" y="560" width="476" height="476" fill="url(#dusk)" role="img" aria-label="Photo of a fairway lined with tall pine trees at sunset"/>
    <ellipse cx="238" cy="430" rx="270" ry="350" fill="var(--navy)" stroke="var(--white)" stroke-width="3"/>
    <rect x="0" y="0" width="476" height="560" fill="var(--navy)"/>
  </svg>

  <h2 class="abs rates-title">Summer Rates</h2>
  <div class="abs band season">May 1 – September 30</div>

  <div class="abs full-box"></div>
  <div class="abs box-label full-title">18 Holes With Cart</div>
  <div class="abs tee-times">7 AM<br>11 AM<br>3 PM</div>
  <div class="abs divider"></div>
  <div class="abs tee-prices">11AM $24<br>3PM $19<br>Close $15</div>

  <div class="abs box-label nine">9 Holes With Cart $15</div>
  <div class="abs box-label walking">Walking $12</div>

  <div class="abs band kids">Children 15 and Under Free<br>with Paid Adult</div>

  <div class="abs lunch">Lunch Available Daily</div>
  <div class="abs lunch-hours">10AM – 3PM</div>

  <div class="abs back-contact" style="top:690px"><svg class="ico" width="16" height="16" viewBox="0 0 16 16"><circle cx="8" cy="8" r="7" fill="none" stroke="var(--white)" stroke-width="1.3"/><path d="M5.5 4.5l1.5 1.6-.8 1c.5 1 1.3 1.8 2.3 2.3l1-.8 1.6 1.5-.9 1.2c-2.6-.4-4.7-2.5-5.1-5.1z" fill="var(--white)"/></svg>555-014-0272</div>
  <div class="abs back-contact" style="top:717px"><svg class="ico" width="14" height="14" viewBox="0 0 14 14"><g fill="none" stroke="var(--white)" stroke-width="1.1"><circle cx="7" cy="7" r="6"/><ellipse cx="7" cy="7" rx="2.6" ry="6"/><path d="M1 7h12M2 4h10M2 10h10"/></g></svg>www.heronbaygc.com</div>

  <div class="abs back-foot"><svg class="ico" width="14" height="18" viewBox="0 0 14 18"><path d="M7 0a7 7 0 0 0-7 7c0 5 7 11 7 11s7-6 7-11a7 7 0 0 0-7-7zm0 10a3 3 0 1 1 0-6 3 3 0 0 1 0 6z" fill="var(--white)"/></svg>The Shores of Heron Bay Golf Club, 2450 NW Cypress Lake Dr<br>Palmview, FL 30012</div>
</section>

</body>
</html>
```